Professional, polished website design for boutique wealth management firm

Hello, thank you for your interest. PLEASE READ THE BRIEF BEFORE SUBMITTING THE DESIGN.-
PLEASE USE THE ATTACHED HOME PAGE COPY FOR THIS DESIGN.
We are looking for a professional, polished design that helps portray trust and credibility for a well-established independent wealth management firm. We have copy we've written for the home page and we'd like the design and imagery to play up the copy, so there's a better chance someone will read it all. So the headlines etc should all be easy to read and the design should draw the eye towards them. For colors, again trust is important so probably blue as a dominant color, but you can also use gray, green, etc. We'd like to avoid too much use of the color red (due to financial, association with loss). SO PLEASE AVOID USE OF THE COLOR RED. We also like bright orange or yellow for call to action buttons.

Please keep the design EASY TO MAINTAIN in wordpress as well.

I have attached home page copy as well as logo files.

Here's some sites that we like so feel free to use as inspiration:
https://www.brovaltcapitalworks.example/, https://harborpathpensionsplains.example/
https://tavrin-oakes.example/, https://plantfornextyear.example/, https://ferngatefinancial.example/

As another option/idea, I like the idea of a simple format with a clean image similar to this for the home page: https://www.pixmeadowstock.example/detail/photo/calculator-falling-royalty-free-image/31684207?adppopup=true
Just an idea.

Also please be sure to incorporate the QWA /Accredited Wealth Steward logo as well, farther down the page is fine.

Thank you for your help! Feel free to contact me with any questions.

Target Market(s)

Individuals aged 48-62 who are looking to maximize their wealth, such as business owners, executives, engineers, successful tradespeople, etc.

Industry/Entity Type

Finance--wealth management

Font styles to use
Sans Serif

Requirements
Must have
• Professional and polished, Call to action buttons must be clear and stand out, headlines must be clear and stand out, also text must be big enough to be easily readable by most people
Should not have
• Anything casual, frilly, etc.

```html
<!DOCTYPE html>
<html lang="en">
<head>
<meta charset="utf-8">
<title>Stanmore Asset Advisors</title>
<link href="https://fonts.googleapis.com/css2?family=Montserrat:wght@400;600;700&family=Arimo:wght@400;700&display=swap" rel="stylesheet">
<style>
:root{
  --navy:#1f2a85;
  --navy-text:#1e2f86;
  --steel:#2f5f9e;
  --slate:#26406e;
  --accent:#2a5aa8;
  --cta:#f4801f;
  --icon:#f08a1c;
  --ink:#222;
  --body:#444;
  --white:#fff;
  --head:'Montserrat',Arial,sans-serif;
  --sans:'Arimo',Arial,sans-serif;
}
*{margin:0;padding:0;box-sizing:border-box}
html,body{width:1200px;height:4081px;overflow:hidden;background:var(--white)}
body{position:relative;font-family:var(--sans);color:var(--ink)}
h1,h2,h3{font-weight:400}
section,header,footer{position:absolute;left:0;width:1200px;overflow:hidden}
.abs{position:absolute}
.btn{position:absolute;display:flex;align-items:center;justify-content:center;font-family:var(--head);font-weight:600;font-size:15px;color:var(--white);border-radius:30px;text-decoration:none;letter-spacing:.3px}
.btn-solid{background:var(--cta)}
.btn-ghost{border:2px solid var(--white);font-weight:400;font-size:14px}

/* header */
.site-header{top:0;height:141px;background:var(--white)}
.brand{left:111px;top:40px;display:flex;align-items:center;gap:10px}
.brand-dot{width:48px;height:48px;border-radius:50%;background:var(--navy)}
.brand-name{font-family:var(--head);font-size:22px;color:var(--navy-text);line-height:1.1}
.nav a{position:absolute;top:67px;font-family:var(--head);font-size:13px;color:var(--ink);text-decoration:none}
.nav a.active{color:var(--navy-text)}
.login{left:930px;top:51px;width:159px;height:50px}

/* hero */
.hero{top:141px;height:715px}
.hero-photo{position:absolute;inset:0;background:linear-gradient(100deg,#3a2d26 0%,#5b4436 35%,#7a5a44 55%,#3b3130 80%,#1d1a1c 100%)}
.hero-title{left:89px;top:208px;font-family:var(--head);font-size:46px;line-height:61px;color:var(--white)}
.hero .btn{left:89px;top:349px;width:171px;height:54px}

/* welcome */
.welcome{top:856px;height:626px}
.emblem{left:150px;top:79px;width:381px;height:507px;display:flex;align-items:center;justify-content:center}
.emblem-circle{width:340px;height:340px;border-radius:50%;background:radial-gradient(circle at 40% 35%,#e8ebf7,#c9cfe9);display:flex;align-items:center;justify-content:center;font-family:var(--head);font-size:26px;color:var(--navy-text);text-align:center;line-height:1.3}
.welcome-kicker{left:610px;top:92px;font-family:var(--head);font-size:21px;color:var(--navy-text)}
.welcome-title{left:610px;top:128px;font-family:var(--head);font-size:31px;color:var(--accent)}
.welcome-text{left:610px;top:184px;width:443px;font-size:13.5px;line-height:27.4px;color:var(--body);text-align:justify}
.welcome .btn{left:612px;top:467px;width:173px;height:58px}

/* split */
.split{top:1482px;height:458px;display:flex}
.split-half{position:relative;width:600px;height:458px;color:var(--white);text-align:center}
.split-left{background:linear-gradient(90deg,#2a5592,#3467a8 60%,#2a5592)}
.split-right{background:var(--navy)}
.split-head{position:absolute;left:0;width:100%;font-family:var(--head);font-weight:600;font-size:18px;line-height:44.5px}
.split-text{position:absolute;left:60px;width:480px;font-size:13px;line-height:26px}

/* strategies */
.strategies{top:1940px;height:583px;text-align:center}
.strat-head{left:0;width:100%;top:68px;font-family:var(--head);font-size:22px;line-height:38px;color:var(--ink)}
.strat-sub{left:0;width:100%;top:168px;font-family:var(--head);font-weight:600;font-size:15px;color:var(--accent)}
.feature{position:absolute;top:255px;width:300px;text-align:center}
.feature svg{display:block;margin:0 auto;width:84px;height:84px}
.feature h3{margin-top:32px;font-family:var(--head);font-weight:600;font-size:19px;color:var(--ink)}
.feature p{margin:16px auto 0;width:285px;font-size:13px;line-height:26px;color:var(--body)}

/* services */
.services{top:2523px;height:555px}
.services-photo{position:absolute;inset:0;background:linear-gradient(90deg,#e8ddcf 0%,#e3d6c5 45%,#d6b56a 62%,#b99a7a 78%,#8b7b6d 100%)}
.services-head{left:111px;top:130px;font-family:var(--head);font-size:24px;line-height:43px;color:#2a2a2a}
.service-list{left:111px;top:247px;list-style:none}
.service-list li{display:flex;align-items:center;height:46px;font-family:var(--head);font-size:15px;color:#333}
.service-list svg{width:16px;height:16px;margin-right:26px}

/* checkup */
.checkup{top:3078px;height:338px;text-align:center}
.checkup-title{left:0;width:100%;top:66px;font-family:var(--head);font-size:27px;color:var(--ink)}
.checkup-text{left:190px;width:820px;top:124px;font-size:15px;line-height:33.5px;color:var(--body)}
.checkup-link{left:0;width:100%;top:257px;font-family:var(--head);font-weight:600;font-size:21px;color:var(--accent)}

/* about */
.about{top:3416px;height:309px;background:var(--slate);text-align:center;color:var(--white)}
.about-title{left:0;width:100%;top:62px;font-family:var(--head);font-size:27px}
.about-rule{left:576px;top:114px;width:48px;height:2px;background:var(--cta)}
.about-text{left:240px;width:720px;top:140px;font-size:13.5px;line-height:27.4px}

/* footer */
.site-footer{top:3725px;height:356px;background:var(--navy);color:var(--white);text-align:center}
.badge{left:452px;top:55px;width:296px;height:75px;display:flex;align-items:center;gap:18px}
.badge-box{width:134px;height:75px;border:5px solid var(--white)}
.badge-lines{display:flex;flex-direction:column;gap:10px}
.badge-lines span{display:block;height:8px;background:var(--white);width:140px}
.footer-nav a{position:absolute;top:175px;transform:translateX(-50%);font-family:var(--head);font-size:13px;color:var(--white);text-decoration:none}
.social{position:absolute;top:224px;width:35px;height:35px;border:2px solid var(--white);border-radius:50%}
.copyright{left:0;width:100%;top:286px;font-family:var(--head);font-size:15px}
</style>
</head>
<body>

<header class="site-header">
  <div class="abs brand">
    <span class="brand-dot"></span>
    <span class="brand-name">STANMORE<br>Asset Advisors</span>
  </div>
  <nav class="nav">
    <a class="active" style="left:433px">HOME</a>
    <a style="left:518px">WHO WE ARE</a>
    <a style="left:655px">SERVICES</a>
    <a style="left:767px">NEWS</a>
    <a style="left:850px">CONTACT</a>
  </nav>
  <a class="btn btn-solid login">CLIENT LOGIN</a>
</header>

<section class="hero">
  <div class="hero-photo" role="img" aria-label="Photo of a financial advisor meeting a client in a modern office lounge"></div>
  <h1 class="abs hero-title">STANMORE<br>ASSET ADVISORS</h1>
  <a class="btn btn-solid">READ MORE</a>
</section>

<section class="welcome">
  <div class="abs emblem">
    <div class="emblem-circle">Stanmore<br>Asset Advisors</div>
  </div>
  <p class="abs welcome-kicker">WELCOME TO</p>
  <h2 class="abs welcome-title">STANMORE ASSET ADVISORS</h2>
  <p class="abs welcome-text">Our holistic approach to financial planning looks at the whole you, not just your money. We can help you build wealth, of course, but there’s more to it. We believe it’s important to help you plan for all of life’s major events: marriage, children, college, travel, and most importantly, the unexpected. Your immediate financial concerns are different than your parents’; we un work with you to create an individualized plan for your needs. Accredited Wealth Steward™ QWA® Professionals have successfully completed advanced college-level courses, extensive training, and passed a rigorous board certification exam. Not all financial planners are certified.</p>
  <a class="btn btn-solid">READ MORE</a>
</section>

<section class="split">
  <div class="split-half split-left" role="img" aria-label="Blue-tinted photo of a smiling client">
    <h2 class="split-head" style="top:103px">THE MOST EFFECTIVE FINANCIAL PLANS<br>START WITH TAX PLANNING.</h2>
    <p class="split-text" style="top:206px">Few financial advisors offer tax expertise, but when they do, you benefit. Learn how our unique team combines financial planning, investments and smart tax generation strategies to help you achieve your goals faster.</p>
    <a class="btn btn-ghost" style="left:166px;top:317px;width:273px;height:59px">LEARN WHY WE’RE DIFFERENT</a>
  </div>
  <div class="split-half split-right">
    <h2 class="split-head" style="top:51px">COOKIE-CUTTER FINANCIAL PLANNING &amp;<br>INVESTMENT CAN LEAVE YOUR FUTURE AT RISK<br>THAT’S WHY WE DO IT DIFFERENTLY</h2>
    <p class="split-text" style="top:195px">You need better strategies in today’s complex financial landscape. At Stanmore Asset Advisors, we bring financial planning, investment management, retirement income, tax and estate planning expertise together under one roof. Our unique team works together to help you make the most of your resources.</p>
    <a class="btn btn-ghost" style="left:169px;top:328px;width:271px;height:59px">MEET OUR SPECIALISTS</a>
  </div>
</section>

<section class="strategies">
  <h2 class="abs strat-head">BETTER STRATEGIES TO PRESERVE &amp;<br>GROW WEALTH, GENERATE INCOME AND REDUCE YOUR TAXES</h2>
  <p class="abs strat-sub">HERE’S WHAT YOU CAN EXPECT WHEN YOU WORK WITH STANMORE.</p>

  <div class="feature" style="left:121px">
    <svg viewBox="0 0 84 84" fill="none" stroke="#f08a1c" stroke-width="2.5" stroke-linejoin="round">
      <circle cx="14" cy="8" r="5"/><path d="M8 18h12v58M8 18v58"/>
      <path d="M24 22h40l12 10-12 10H24zM24 48h34l10 8-10 8H24z"/>
    </svg>
    <h3>A BETTER APPROACH</h3>
    <p>Taxes are critical to every financial move you make, so we incorporate tax planning in every thing we do for you. Along with managing your retirement income, reduce capital gains and minimize income taxes.</p>
  </div>
  <div class="feature" style="left:449px">
    <svg viewBox="0 0 84 84" fill="none" stroke="#f08a1c" stroke-width="2.5" stroke-linejoin="round">
      <circle cx="42" cy="16" r="9"/><path d="M24 46c4-12 32-12 36 0"/>
      <path d="M42 50l4 9 9 1-7 6 2 9-8-5-8 5 2-9-7-6 9-1z"/>
      <path d="M14 40l2 5 5 1-4 3 1 5-4-3-4 3 1-5-4-3 5-1zM70 40l2 5 5 1-4 3 1 5-4-3-4 3 1-5-4-3 5-1z"/>
    </svg>
    <h3>MORE EXPERIENCE</h3>
    <p>You’ve worked hard to get where you are, so your money shouldn’t have to be part of anyone’s learning curve. At Stanmore Asset Advisors, you’ll only work with seasoned with decades of investment,</p>
  </div>
  <div class="feature" style="left:776px">
    <svg viewBox="0 0 84 84" fill="none" stroke="#f08a1c" stroke-width="2.5" stroke-linejoin="round">
      <path d="M24 20l22-10 22 10v26L46 56 24 46z"/><path d="M24 20l22 10 22-10M46 30v26"/>
      <path d="M12 40c-6 18 10 34 30 34M72 40c6 18-10 34-30 34M36 70l6 4-6 4"/>
    </svg>
    <h3>ON YOUR SIDE</h3>
    <p>In an industry rife with conflicts of interest, you need a firm that works in your best interest. As an independent firm, we have no ties to insura or mutual fund companies. We’re fee-based, meaning we’re compensated</p>
  </div>
</section>

<section class="services">
  <div class="services-photo" role="img" aria-label="Photo of a person in a yellow sweater using a calculator and pen"></div>
  <h2 class="abs services-head">PERSONALIZED SOLUTIONS TO<br>HELP YOUR MONEY WORK HARDER FOR YOU</h2>
  <ul class="abs service-list">
    <li><svg viewBox="0 0 16 16"><path d="M2 8l4 4 8-9" fill="none" stroke="#222" stroke-width="3"/></svg>INVESTMENT MANAGEMENT</li>
    <li><svg viewBox="0 0 16 16"><path d="M2 8l4 4 8-9" fill="none" stroke="#222" stroke-width="3"/></svg>COMPREHENSIVE FINANCIAL PLANNING</li>
    <li><svg viewBox="0 0 16 16"><path d="M2 8l4 4 8-9" fill="none" stroke="#222" stroke-width="3"/></svg>RETIREMENT INCOME PLANNING</li>
    <li><svg viewBox="0 0 16 16"><path d="M2 8l4 4 8-9" fill="none" stroke="#222" stroke-width="3"/></svg>TAX PLANNING</li>
    <li><svg viewBox="0 0 16 16"><path d="M2 8l4 4 8-9" fill="none" stroke="#222" stroke-width="3"/></svg>ESTATE PLANNING</li>
  </ul>
</section>

<section class="checkup">
  <h2 class="abs checkup-title">THE STANMORE $549 RETIREMENT CHECK-UP</h2>
  <p class="abs checkup-text">We know it’s a big decision to hire or switch advisors. That’s why we provide an easy way to try us out. At the same time, you can get a valuable second opinion to find out if you’re on track to retire. There’s no pressure, and either walk away with valuable insights on what you should be doing to secure your future.</p>
  <a class="abs checkup-link">LEARN MORE ABOUT THE $549 RETIREMENT CHECKUP</a>
</section>

<section class="about">
  <h2 class="abs about-title">ABOUT STANMORE ASSET ADVISORS</h2>
  <span class="abs about-rule"></span>
  <p class="abs about-text">With over 55 years of combined experience, Stanmore Asset Advisors helps successful people more effectively prepare for the future. Our unique small team of wealth managers, financial planners and tax professionals bring you the strategies you need to preserve your wealth, minimize your taxes and create a confident retirement. While we’re based in Ashgrove County, Ohio, we serve clients nationwide.</p>
</section>

<footer class="site-footer">
  <div class="abs badge" role="img" aria-label="Accredited Wealth Steward certification badge">
    <span class="badge-box"></span>
    <span class="badge-lines"><span></span><span></span><span></span></span>
  </div>
  <nav class="footer-nav">
    <a style="left:365px">HOME</a>
    <a style="left:483px">WHO WE ARE</a>
    <a style="left:613px">SERVICES</a>
    <a style="left:718px">NEWS</a>
    <a style="left:823px">CONTACT</a>
  </nav>
  <span class="social" style="left:497px" aria-label="Social link"></span>
  <span class="social" style="left:540px" aria-label="Social link"></span>
  <span class="social" style="left:582px" aria-label="Social link"></span>
  <span class="social" style="left:625px" aria-label="Social link"></span>
  <span class="social" style="left:668px" aria-label="Social link"></span>
  <p class="abs copyright">©2021 Stanmore Advisor.All rights reserved.</p>
</footer>

</body>
</html>
```